Need 2 sided card for Loomfield Goods Co. Logo supplied.

I am looking for a business card for my online craft supply business.

I have a very simple design already which I am kind of happy with (see attached pdf) - but would like suggestions for something a little more creative. Design MUST be clean. Super clean! Think thin lines and not blocks of color...

Design must be clean and crisp. No other colors other than in palette (see link below)

I would also like to possible incorporate my tagline - maybe on the front but definitely on the back:
"HobbyNest Ideas & Making Materials"

Logo file is supplied, but I think spacing on the card may required the wording to be moved underneaths the camera icon - which is fine. Font in logo is Maven Pro. OPEN TO USE OF OTHER FONTS ON CARD BUT MUST BE CLEAN DESIGN.

FRONT OF CARD
All information on attached pdf is correct and should be shown in your design.

BACK OF CARD
Needs to show www.tinselbrookstore.com and maybe logo repeat and tagline.

SIZE
New Zealand sized - meaning finished card will be 90 x 55mm
Printing requirements: printed area is 90mm x 55mm with a 2mm bleed all round.

COLORS
Color palette used in logo can be seen here for HEX and RGB reference: http://www.huegatherly.net/palette/8802417/website

NOTE: PAYMENT WILL BE MADE FOR THE BEST DESIGN - EVEN IF I DECIDE NOT TO USE IT.
Updates

Thank you all so much for your designs. I will be providing feedback to ALL designers tomorrow. This weekend is a holiday weekend here in New Zealand and so no work for a few days. Thank-you again - I appreciate your time and creativity!

Industry/Entity Type

Camera

Font styles to use
Other font styles liked:
• Maven Pro - open to others

Requirements
Must have
• Clean design. Logo must be prominent for brand recognition. All contact information must be shown.
Nice to have
• Tagline - at least on reverse

```html
<!DOCTYPE html>
<html lang="en">
<head>
<meta charset="utf-8">
<title>Loomfield Goods Co. – Business Card</title>
<link href="https://fonts.googleapis.com/css2?family=Maven+Pro:wght@400;500&family=Ubuntu:wght@400;700&display=swap" rel="stylesheet">
<style>
  :root {
    --stone: #5f5854;
    --citron: #d4c400;
    --ember: #e8572a;
    --sea: #5fa89a;
    --paper: #ffffff;
    --canvas: #ffffff;
  }
  * { box-sizing: border-box; margin: 0; padding: 0; }
  html, body { width: 848px; height: 1200px; overflow: hidden; background: var(--canvas); }
  body { position: relative; font-family: "Ubuntu", sans-serif; color: var(--stone); }

  .card {
    position: absolute;
    left: 88px;
    width: 689px;
    height: 421px;
    background: var(--paper);
    box-shadow: 0 6px 14px rgba(0,0,0,0.28);
    overflow: hidden;
  }

  /* Front */
  .card-front { top: 100px; }
  .front-brand {
    position: absolute;
    left: 0; right: 0; top: 96px;
    text-align: center;
  }
  .brand-dot {
    display: block;
    width: 58px; height: 58px;
    margin: 0 auto 22px;
    border-radius: 50%;
    background: var(--ember);
  }
  .brand-name {
    font-family: "Maven Pro", sans-serif;
    font-weight: 400;
    color: var(--stone);
    letter-spacing: -0.5px;
    line-height: 1;
  }
  .front-brand .brand-name { font-size: 48px; }
  .front-tagline {
    margin-top: 10px;
    font-family: "Ubuntu", sans-serif;
    font-size: 12px;
    color: var(--stone);
  }
  .front-band {
    position: absolute;
    left: 0; right: 0; bottom: 0;
    height: 35px;
    background: var(--stone);
    text-align: center;
    font-size: 20px;
    line-height: 35px;
    color: var(--paper);
  }
  .front-band .accent { color: var(--citron); }

  /* Back */
  .card-back { top: 668px; background: var(--stone); }
  .back-panel {
    position: absolute;
    left: 0; top: 0;
    width: 689px; height: 354px;
    background: var(--paper);
    border-radius: 0 0 82px 82px;
  }
  .back-brand {
    position: absolute;
    left: 40px; top: 96px;
    width: 276px;
    text-align: center;
  }
  .back-brand .brand-dot { width: 46px; height: 46px; margin-bottom: 16px; }
  .back-brand .brand-name { font-size: 27px; }
  .back-divider {
    position: absolute;
    left: 319px; top: 72px;
    width: 2px; height: 202px;
    background: var(--stone);
  }
  .contact-list {
    position: absolute;
    left: 338px; top: 80px;
    list-style: none;
  }
  .contact-item {
    display: flex;
    align-items: center;
    height: 31px;
    font-size: 19px;
    color: var(--stone);
  }
  .contact-icon {
    width: 24px; height: 24px;
    margin-right: 10px;
    flex: none;
  }
  .holder-name {
    position: absolute;
    left: 0; right: 0; bottom: 0;
    height: 66px;
    text-align: center;
    line-height: 66px;
    font-family: "Ubuntu", sans-serif;
    font-weight: 700;
    font-size: 30px;
    color: var(--paper);
  }
</style>
</head>
<body>

<section class="card card-front" aria-label="Card front">
  <div class="front-brand">
    <span class="brand-dot"></span>
    <div class="brand-name">Loomfield Goods Co.</div>
    <div class="front-tagline">HobbyNest Ideas &amp; Making Materials</div>
  </div>
  <div class="front-band">
    <span class="accent">www.</span>tinselbrookstore<span class="accent">.com</span>
  </div>
</section>

<section class="card card-back" aria-label="Card back">
  <div class="back-panel">
    <div class="back-brand">
      <span class="brand-dot"></span>
      <div class="brand-name">Loomfield Goods Co.</div>
    </div>
    <div class="back-divider"></div>
    <ul class="contact-list">
      <li class="contact-item">
        <svg class="contact-icon" viewBox="0 0 24 24" aria-hidden="true">
          <circle cx="12" cy="12" r="12" fill="var(--ember)"/>
          <path d="M8 6.5c-1 .6-1.6 1.6-1.2 3 1 3.4 3.6 6 7 7 1.4.4 2.4-.2 3-1.2l-2.3-1.8-1.4 1c-1.6-.7-2.9-2-3.6-3.6l1-1.4z" fill="#fff"/>
        </svg>
        +64 (0) 3 555 0142
      </li>
      <li class="contact-item">
        <svg class="contact-icon" viewBox="0 0 24 24" aria-hidden="true">
          <circle cx="12" cy="12" r="12" fill="var(--citron)"/>
          <rect x="8.5" y="5.5" width="7" height="13" rx="1.5" fill="#fff"/>
          <rect x="9.7" y="7.2" width="4.6" height="8" fill="var(--citron)"/>
        </svg>
        +64 (0) 21 555 01876
      </li>
      <li class="contact-item">
        <svg class="contact-icon" viewBox="0 0 24 24" aria-hidden="true">
          <circle cx="12" cy="12" r="12" fill="var(--sea)"/>
          <rect x="6" y="8" width="12" height="8.5" rx="1" fill="#fff"/>
          <path d="M6.3 8.5 12 13l5.7-4.5" fill="none" stroke="var(--sea)" stroke-width="1.3"/>
        </svg>
        mara.ellison@loomfieldnz.com
      </li>
      <li class="contact-item">
        <svg class="contact-icon" viewBox="0 0 24 24" aria-hidden="true">
          <circle cx="12" cy="12" r="12" fill="var(--stone)"/>
        </svg>
        loomfield.social/goods
      </li>
      <li class="contact-item">
        <svg class="contact-icon" viewBox="0 0 24 24" aria-hidden="true">
          <circle cx="12" cy="12" r="12" fill="var(--sea)"/>
          <path d="M7 18v-6a5 5 0 0 1 10 0v6h-2.5v-5.5a2.5 2.5 0 0 0-5 0V18z" fill="#fff"/>
        </svg>
        www.tinselbrookstore.com
      </li>
      <li class="contact-item">
        <svg class="contact-icon" viewBox="0 0 24 24" aria-hidden="true">
          <circle cx="12" cy="12" r="12" fill="var(--ember)"/>
          <g fill="none" stroke="#fff" stroke-width="1.3">
            <circle cx="12" cy="12" r="6"/>
            <ellipse cx="12" cy="12" rx="2.6" ry="6"/>
            <path d="M6 12h12M7 9h10M7 15h10"/>
          </g>
        </svg>
        www.loomfieldnz.com
      </li>
    </ul>
  </div>
  <div class="holder-name">Mara Ellison</div>
</section>

</body>
</html>
```